81M business card

I need a business card for a life sciences consulting firm I started. The company name is 81M and the logo is attached. I am looking for something edgey and current but different from the blah standard business card.

Industry/Entity Type

Business

Requirements
Nice to have
• Both sides

```html
<!DOCTYPE html>
<html lang="en">
<head>
<meta charset="utf-8">
<title>81M LLC Business Card</title>
<link rel="stylesheet" href="https://fonts.googleapis.com/css2?family=Questrial&display=swap">
<style>
  :root {
    --stage: #e9ebef;
    --card-white: #ffffff;
    --navy: #0e2a7a;
    --orange: #f08a24;
    --ink: #3a3a3a;
    --muted: #6f7480;
    --faint: rgba(14, 42, 122, 0.07);
  }
  * { box-sizing: border-box; margin: 0; padding: 0; }
  html, body {
    width: 1200px; height: 675px; overflow: hidden;
    background: var(--stage);
    font-family: "Questrial", "Century Gothic", sans-serif;
  }
  .stage {
    width: 1200px; height: 675px;
    display: flex; align-items: center; justify-content: center; gap: 40px;
  }
  .card {
    position: relative;
    width: 520px; height: 297px;
    overflow: hidden;
    box-shadow: 0 10px 28px rgba(0,0,0,0.18);
  }
  .card-front { background: var(--card-white); }
  .card-back { background: var(--navy); display: flex; align-items: center; justify-content: center; }

  .brand { display: flex; align-items: center; gap: 10px; }
  .brand-mark { width: 40px; height: 40px; border-radius: 50%; background: var(--navy); flex: none; }
  .brand-name { font-size: 38px; color: var(--navy); line-height: 1; letter-spacing: 1px; }
  .brand-tagline { font-size: 9.5px; color: var(--muted); margin-top: 3px; letter-spacing: 0.3px; }

  .card-front .brand { position: absolute; left: 30px; top: 56px; }
  .front-deco {
    position: absolute; right: -30px; top: -150px;
    width: 270px; height: 270px; border-radius: 50%;
    background: var(--faint);
  }

  .person { position: absolute; left: 178px; top: 148px; }
  .person-name { color: var(--orange); font-size: 15px; font-weight: 700; }
  .person-title { color: var(--ink); font-size: 12px; margin-top: 1px; }

  .contact-list { list-style: none; position: absolute; left: 178px; top: 202px; }
  .contact-list li {
    display: flex; align-items: center; gap: 6px;
    color: var(--ink); font-size: 11.5px; line-height: 17px;
  }
  .contact-list svg { width: 10px; height: 10px; fill: var(--orange); flex: none; }

  .address {
    position: absolute; left: 345px; top: 148px;
    color: var(--ink); font-size: 11.5px; line-height: 16px; font-style: normal;
  }
  .address .web { color: var(--navy); font-weight: 700; }

  .card-back .brand-name { color: var(--card-white); font-size: 46px; }
  .card-back .brand-mark { background: var(--card-white); width: 50px; height: 50px; }
  .card-back .brand-tagline { color: rgba(255,255,255,0.85); font-size: 10.5px; }
</style>
</head>
<body>
<main class="stage">
  <section class="card card-front" aria-label="Card front">
    <div class="front-deco" aria-hidden="true"></div>
    <div class="brand">
      <span class="brand-mark" aria-hidden="true"></span>
      <div>
        <div class="brand-name">81M LLC</div>
        <div class="brand-tagline">regulatory consulting and contract services</div>
      </div>
    </div>

    <div class="person">
      <div class="person-name">Nora Vance</div>
      <div class="person-title">Principal</div>
    </div>

    <ul class="contact-list">
      <li><svg viewBox="0 0 10 10"><path d="M1 3 Q5 0 9 3 L8 4.5 L6.5 3.8 L6.5 3 Q5 2.6 3.5 3 L3.5 3.8 L2 4.5 Z M2.5 5 H7.5 L8.5 9 H1.5 Z"/></svg>+1.555.0142867</li>
      <li><svg viewBox="0 0 10 10"><path d="M1 3 Q5 0 9 3 L8 4.5 L6.5 3.8 L6.5 3 Q5 2.6 3.5 3 L3.5 3.8 L2 4.5 Z M2.5 5 H7.5 L8.5 9 H1.5 Z"/></svg>+1.555.0193344 (x418) - Direct</li>
      <li><svg viewBox="0 0 10 10"><path d="M0.5 2 H9.5 V8.5 H0.5 Z M0.5 2 L5 5.5 L9.5 2" stroke="#fff" stroke-width="0.8"/></svg>nora@81mllc.com</li>
    </ul>

    <address class="address">
      4180 Harbor Crest Drive<br>
      Lindale, California 90417<br>
      <span class="web">www.81mllc.com</span>
    </address>
  </section>

  <section class="card card-back" aria-label="Card back">
    <div class="brand">
      <span class="brand-mark" aria-hidden="true"></span>
      <div>
        <div class="brand-name">81M LLC</div>
        <div class="brand-tagline">regulatory consulting and contract services</div>
      </div>
    </div>
  </section>
</main>
</body>
</html>
```